Stationery Design
Letterhead, Envelope, Business Card, Email signature design
I need single sided standard sized Business Card [3.5" x 2"]
Myriad Pro
Professional
Corisse Pallant
Brand Manager
4127 Dunford Avenue
Burnaby, B.C. V3K 8T2
604-281-7734 ext. 120
corisse@brightfernco.ca
brightfernco.ca
We are a family-owned school photography company in Western Canada. We've just had a new logo and website designed and need some new stationery.
This is the .ai file we would like to use for the stationery design. Please refer to our website, brightfernco.ca, for more information about our brand.

```html
<!DOCTYPE html>
<html lang="en">
<head>
<meta charset="utf-8">
<title>Bright Fern Co – Business Cards</title>
<link href="https://fonts.googleapis.com/css2?family=Source+Sans+3:wght@400;600;700&display=swap" rel="stylesheet">
<style>
  :root {
    --brand-blue: #2aa3cb;
    --ink: #3a3a3a;
    --muted: #6d6d6d;
    --paper: #f7f8f8;
    --paper-edge: #dfe3e5;
    --night: #0d0e10;
    --night-text: #8a8d90;
    --stage: #e9eaeb;
    --photo-warm: #8a5a48;
    --photo-cool: #c9c3bd;
  }
  html, body {
    margin: 0;
    padding: 0;
    width: 1200px;
    height: 737px;
    overflow: hidden;
    background: var(--stage);
    font-family: "Source Sans 3", "Myriad Pro", Arial, sans-serif;
  }
  .sheet { position: relative; width: 1200px; height: 737px; }

  .card {
    position: absolute;
    width: 474px;
    height: 270px;
    border-radius: 12px;
    overflow: hidden;
    box-shadow: 0 2px 6px rgba(0,0,0,0.18);
  }
  .card--light { background: linear-gradient(180deg, #ffffff 0%, var(--paper) 60%, var(--paper-edge) 100%); color: var(--ink); }
  .card--dark  { background: var(--night); color: var(--night-text); }

  .front-light { left: 120px; top: 91px; }
  .front-dark  { left: 606px; top: 91px; }
  .back-light  { left: 120px; top: 378px; }
  .back-dark   { left: 606px; top: 378px; }

  .brand {
    position: absolute;
    left: 26px;
    top: 24px;
    display: flex;
    align-items: center;
    gap: 10px;
  }
  .brand__mark { width: 30px; height: 30px; background: var(--brand-blue); }
  .brand__name {
    font-size: 30px;
    font-weight: 700;
    letter-spacing: -0.5px;
    line-height: 1;
    color: var(--ink);
  }
  .card--dark .brand__name { color: #f2f2f2; }

  .contact { position: absolute; left: 26px; }
  .front-light .contact { top: 112px; }
  .front-dark .contact  { top: 112px; }
  .contact__name  { margin: 0; font-size: 14px; font-weight: 600; color: var(--brand-blue); }
  .contact__title { margin: 0 0 12px; font-size: 13px; }
  .contact__line  { margin: 0; font-size: 10.5px; line-height: 15px; }
  .contact__line b { color: var(--brand-blue); font-weight: 600; }
  .contact__address { margin: 0 0 10px; font-size: 10.5px; }

  .web {
    position: absolute;
    font-size: 13px;
    font-weight: 600;
    letter-spacing: 2.5px;
    color: var(--brand-blue);
  }
  .front-light .web { left: 26px; bottom: 14px; }

  .portrait {
    position: absolute;
    background: linear-gradient(160deg, var(--photo-cool) 0%, var(--photo-warm) 70%, #5d3b30 100%);
  }
  .front-light .portrait { right: 0; top: 0; width: 132px; height: 156px; }
  .front-dark .portrait  { right: 10px; bottom: 0; width: 110px; height: 156px; }

  .corner-mark {
    position: absolute;
    right: 28px;
    bottom: 22px;
    width: 54px;
    height: 54px;
    background: var(--brand-blue);
  }

  .back-mark {
    position: absolute;
    left: 50%;
    top: 62px;
    width: 100px;
    height: 100px;
    margin-left: -50px;
    background: var(--brand-blue);
  }
  .back-light .web, .back-dark .web {
    left: 0; right: 0; bottom: 30px;
    text-align: center;
    font-size: 15px;
    letter-spacing: 4px;
  }
</style>
</head>
<body>
<main class="sheet">

  <section class="card card--light front-light">
    <div class="brand"><span class="brand__mark"></span><span class="brand__name">BRIGHTFERN CO</span></div>
    <div class="portrait" role="img" aria-label="Portrait photograph of Corisse Pallant"></div>
    <div class="contact">
      <p class="contact__name">Corisse Pallant</p>
      <p class="contact__title">Brand Manager</p>
      <p class="contact__address">4127 Dunford Avenue, Burnaby, B.C. V3K 8T2</p>
      <p class="contact__line"><b>T:</b> 1-888-502-3190 &nbsp;|&nbsp; <b>P:</b> 604-281-7734 ext. 120</p>
      <p class="contact__line"><b>C:</b> 604-719-2248 &nbsp;|&nbsp; <b>F:</b> 604-281-7790</p>
      <p class="contact__line"><b>E:</b> corisse@brightfernco.ca</p>
    </div>
    <span class="corner-mark"></span>
    <span class="web">brightfernco.ca</span>
  </section>

  <section class="card card--dark front-dark">
    <div class="brand"><span class="brand__mark"></span><span class="brand__name">BRIGHTFERN CO</span></div>
    <div class="contact">
      <p class="contact__name">Corisse Pallant</p>
      <p class="contact__title">Brand Manager</p>
      <p class="contact__address">4127 Dunford Avenue, Burnaby, B.C. V3K 8T2</p>
      <p class="contact__line"><b>T:</b> 1-888-502-3190 &nbsp;|&nbsp; <b>P:</b> 604-281-7734 ext. 120</p>
      <p class="contact__line"><b>C:</b> 604-719-2248 &nbsp;|&nbsp; <b>F:</b> 604-281-7790</p>
      <p class="contact__line"><b>E:</b> corisse@brightfernco.ca</p>
    </div>
    <div class="portrait" role="img" aria-label="Portrait photograph of Corisse Pallant"></div>
  </section>

  <section class="card card--light back-light">
    <span class="back-mark"></span>
    <span class="web">brightfernco.ca</span>
  </section>

  <section class="card card--dark back-dark">
    <span class="back-mark"></span>
    <span class="web">brightfernco.ca</span>
  </section>

</main>
</body>
</html>
```